We need an attractive, simple & modern / Aussie Design of BusinessCard using the existing company Logo.
Our company is located in Perth, WA, Australia.
The Company name is Tarn Vale Construction & Maintenance
Name on the card is Dorian Pelk
Designation is Managing Director
Building Registration BC584731
M: 0438 517 362
E: tarnvaleconstruction@mailhub.example

Our main tasks are Building new homes, medical centers, mixed use. Renovations & Maintenance.

Slogan: Let Quality Meets Your Budget (We are open if you please suggest something more attractive within same concept)

Target Market(s)

Individuals to build or renovate homes, Doctors and dentists to build, renovate, fit off clinics and medical centres, Schools & real estate offices for maintenance contracts.

Industry/Entity Type

Construction

Contact Information for Business Card

To contain company name, logo, person name and contact details, building registration detail, slogan and to give brief on our services

Colors

Designer to choose colors to be used in the design.

Requirements
Must have
• To have attractive design. And contain company name, logo, person name, designation and contact details, building registration detail, slogan and to give brief on our services.
• Elegant and Simple Style.
Nice to have
• Modern Aussie style.
Should not have
• Should not be too much busy or complicated.

```html
<!DOCTYPE html>
<html lang="en">
<head>
<meta charset="utf-8">
<title>Tarn Vale Construction &amp; Maintenance – Business Card</title>
<link rel="stylesheet" href="https://fonts.googleapis.com/css2?family=Open+Sans:wght@400;600;700;800&display=swap">
<style>
  :root {
    --stage: #2b2b2b;
    --card-black: #111111;
    --card-white: #ffffff;
    --orange: #f37021;
    --ink: #1a1a1a;
    --muted: #9a9a9a;
    --light: #f2f2f2;
  }
  * { box-sizing: border-box; margin: 0; padding: 0; }
  html, body {
    width: 1200px; height: 660px; overflow: hidden;
    background: var(--stage);
    font-family: "Open Sans", Arial, sans-serif;
  }
  .stage {
    position: relative; width: 1200px; height: 660px;
    display: flex; align-items: center; justify-content: center; gap: 40px;
  }
  .card {
    position: relative; width: 540px; height: 310px; overflow: hidden;
    box-shadow: 0 10px 30px rgba(0,0,0,.45);
  }

  /* Front */
  .card--front { background: var(--card-black); color: var(--light); }
  .brand {
    display: flex; align-items: center; gap: 10px;
  }
  .brand__mark { width: 14px; height: 14px; background: var(--orange); flex: none; }
  .brand__name {
    font-weight: 800; text-transform: uppercase; line-height: 1.05;
  }
  .card--front .brand {
    position: absolute; left: 0; right: 0; top: 62px; justify-content: center;
  }
  .card--front .brand__name { color: var(--light); font-size: 26px; text-align: center; }
  .card--front .brand__name small { display: block; font-size: 11px; letter-spacing: 1.2px; }
  .slogan {
    position: absolute; top: 142px; left: 0; right: 0; text-align: center;
    font-size: 12px; font-weight: 600; color: var(--light);
  }
  .slogan::before, .slogan::after {
    content: ""; display: inline-block; width: 24px; height: 1px;
    background: var(--light); vertical-align: middle; margin: 0 8px;
  }
  .rule { position: absolute; left: 22px; right: 22px; height: 1px; background: var(--orange); }
  .rule--top { top: 218px; }
  .rule--bottom { top: 258px; }
  .services {
    position: absolute; top: 228px; left: 0; right: 0; text-align: center;
    font-size: 10.5px; font-weight: 600; letter-spacing: .3px; text-transform: uppercase;
  }

  /* Back */
  .card--back { background: var(--card-white); color: var(--ink); }
  .card--back .brand { position: absolute; left: 38px; top: 112px; }
  .card--back .brand__name { color: var(--ink); font-size: 24px; }
  .card--back .brand__name small { display: block; font-size: 10px; letter-spacing: 1px; }
  .divider {
    position: absolute; left: 262px; top: 38px; width: 1px; height: 140px; background: var(--muted);
  }
  .contact { position: absolute; left: 282px; top: 40px; }
  .contact__name { font-size: 17px; font-weight: 600; text-transform: uppercase; letter-spacing: .3px; }
  .contact__role { font-size: 11px; font-weight: 600; color: var(--orange); margin-bottom: 14px; }
  .contact__row { display: flex; align-items: center; gap: 8px; font-size: 10.5px; margin-bottom: 6px; }
  .contact__row svg { width: 12px; height: 12px; flex: none; }
  .contact__company { font-size: 10.5px; font-weight: 700; color: var(--orange); margin-top: 8px; }
  .contact__city { font-size: 10.5px; }
  .footer-band { position: absolute; left: 0; bottom: 0; width: 540px; height: 80px; }
  .registration {
    position: absolute; right: 16px; bottom: 52px;
    font-size: 12px; font-weight: 700; letter-spacing: 1px; color: var(--orange);
  }
</style>
</head>
<body>
<main class="stage">
  <section class="card card--front" aria-label="Card front">
    <div class="brand">
      <span class="brand__mark"></span>
      <div class="brand__name">Tarn Vale<small>Construction &amp; Maintenance</small></div>
    </div>
    <p class="slogan">Let Quality Meets Your Budget</p>
    <div class="rule rule--top"></div>
    <p class="services">Building New Homes • Medical Centers • Mixed Use • Renovations &amp; Maintenance</p>
    <div class="rule rule--bottom"></div>
  </section>

  <section class="card card--back" aria-label="Card back">
    <div class="brand">
      <span class="brand__mark"></span>
      <div class="brand__name">Tarn Vale<small>Construction &amp; Maintenance</small></div>
    </div>
    <div class="divider"></div>
    <div class="contact">
      <p class="contact__name">Dorian Pelk</p>
      <p class="contact__role">Managing Director</p>
      <p class="contact__row">
        <svg viewBox="0 0 12 12" aria-hidden="true"><rect x="3" y="0.5" width="6" height="11" rx="1.2" fill="none" stroke="var(--orange)" stroke-width="1.2"/><rect x="5" y="9" width="2" height="1" fill="var(--orange)"/></svg>
        0438 517 362
      </p>
      <p class="contact__row">
        <svg viewBox="0 0 12 12" aria-hidden="true"><rect x="0.5" y="2" width="11" height="8" fill="var(--orange)"/><path d="M0.5 2 L6 7 L11.5 2" fill="none" stroke="#fff" stroke-width="1"/></svg>
        tarnvaleconstruction@mailhub.example
      </p>
      <p class="contact__company">Tarn Vale Construction &amp; Maintenance</p>
      <p class="contact__city">Perth, WA, Australia</p>
    </div>
    <svg class="footer-band" viewBox="0 0 540 80" aria-hidden="true">
      <path d="M0,72 L540,44 L540,80 L0,80 Z" fill="var(--orange)"/>
      <path d="M400,52 L400,20 Q400,8 414,8 L540,8 L540,44 Z" fill="var(--card-black)"/>
    </svg>
    <p class="registration">BC584731</p>
  </section>
</main>
</body>
</html>
```